Event flyer for Sunday night Youth Group

Need a 4 x 6 or 5 x 7 flyer for a new youth group starting on April 14. The youth group is for students in middle school and high school so it needs to look fun and cool, but not childish. I prefer it not to include pictures of people unless it's so obscure you can't really see their faces. I've uploaded some pictures of flyers I like. I've also attached a couple versions of our logo to use on the flyer.
Information the flyer needs to include:
Youth Group
Sundays, 6-8pm (beginning April 14)
Location: Wexlander's - 4182 Quillon Ridge Ave N, Keizer, 97158
There will be dinner, games, friends, and a message.
Target Market(s)
Youth ages 13-18
Industry/Entity Type
Church
Colors
Look and feel

```html
<!DOCTYPE html>
<html lang="en">
<head>
<meta charset="utf-8">
<title>Youth Group Flyer</title>
<link rel="stylesheet" href="https://fonts.googleapis.com/css2?family=Poppins:wght@400;500;600;700;800&family=Yellowtail&display=swap">
<style>
  :root {
    --page-bg: #d9d9d9;
    --flyer-deep: #03100f;
    --flyer-teal: #0d4a44;
    --flyer-glow: #2f8f82;
    --white: #ffffff;
    --orange: #ffb21c;
    --orange-deep: #f08a00;
    --ink: #1a1a1a;
    --tag-blue: #19b8f0;
    --hex-line: rgba(190, 240, 230, 0.75);
  }
  * { margin: 0; padding: 0; box-sizing: border-box; }
  html, body { width: 1200px; height: 2400px; overflow: hidden; }
  body {
    background: var(--page-bg);
    font-family: "Poppins", sans-serif;
    position: relative;
  }
  .flyer {
    position: absolute;
    left: 50px; top: 409px;
    width: 1100px; height: 1582px;
    overflow: hidden;
    background:
      radial-gradient(ellipse 70% 45% at 50% 30%, rgba(47,143,130,0.55), transparent 70%),
      linear-gradient(180deg, var(--flyer-teal) 0%, #082c29 45%, var(--flyer-deep) 100%);
    box-shadow: 0 18px 40px rgba(0,0,0,0.25);
  }
  .crowd-area {
    position: absolute;
    left: 0; right: 0; top: 780px; height: 520px;
    background: linear-gradient(180deg, rgba(3,16,15,0) 0%, rgba(2,10,10,0.85) 55%, rgba(3,16,15,0.2) 100%);
  }
  .brand {
    position: absolute;
    top: 140px; left: 0; right: 0;
    display: flex; justify-content: center; align-items: center; gap: 22px;
  }
  .brand-square { width: 48px; height: 48px; background: var(--white); }
  .brand-name {
    color: var(--white); font-weight: 500; font-size: 40px;
    letter-spacing: 3px; line-height: 1.1;
  }
  .hex-frame { position: absolute; left: 307px; top: 300px; width: 486px; height: 470px; }
  .title-script {
    position: absolute; top: 380px; left: 0; right: 0; text-align: center;
    font-family: "Yellowtail", cursive; font-size: 190px; line-height: 1;
    background: linear-gradient(180deg, var(--orange) 20%, var(--orange-deep) 90%);
    -webkit-background-clip: text; background-clip: text; color: transparent;
    transform: rotate(-6deg);
  }
  .title-main {
    position: absolute; top: 575px; left: 0; right: 0; text-align: center;
    color: var(--white); font-weight: 800; font-size: 140px; line-height: 1; letter-spacing: 2px;
  }
  .schedule {
    position: absolute; top: 1130px; left: 0; right: 0; text-align: center;
    color: var(--white); font-weight: 700; font-size: 68px; line-height: 1; letter-spacing: 1px;
  }
  .start-date {
    position: absolute; top: 1220px; left: 0; right: 0; text-align: center;
    color: var(--white); font-weight: 400; font-size: 36px; letter-spacing: 6px;
  }
  .location-bar {
    position: absolute; top: 1300px; left: 127px; width: 931px; height: 60px;
    background: linear-gradient(90deg, var(--orange), var(--orange-deep));
    display: flex; align-items: center; gap: 14px; padding-left: 26px;
    color: var(--ink); font-weight: 600; font-size: 28px;
  }
  .location-bar svg { width: 30px; height: 38px; flex: none; }
  .offer-label {
    position: absolute; top: 1418px; left: 0; right: 0; text-align: center;
    color: var(--white); font-weight: 500; font-size: 22px; letter-spacing: 7px;
  }
  .offer-tags {
    position: absolute; top: 1470px; left: 72px; width: 986px;
    display: flex; justify-content: space-between;
  }
  .offer-tag {
    width: 232px; height: 48px; background: var(--tag-blue);
    transform: skewX(-18deg);
    display: flex; align-items: center; justify-content: center;
  }
  .offer-tag span {
    transform: skewX(18deg);
    color: var(--ink); font-weight: 700; font-size: 28px; letter-spacing: 2px;
  }
</style>
</head>
<body>
  <main class="flyer">
    <div class="crowd-area" role="img" aria-label="Silhouetted concert crowd with raised hands, faces not visible"></div>

    <header class="brand">
      <div class="brand-square"></div>
      <div class="brand-name">HARBORLINE FELLOWSHIP</div>
    </header>

    <svg class="hex-frame" viewBox="0 0 486 470" aria-hidden="true">
      <polygon points="121,8 365,8 478,235 365,462 121,462 8,235" fill="none" stroke="var(--hex-line)" stroke-width="5"/>
      <polygon points="132,26 354,26 458,235 354,444 132,444 28,235" fill="none" stroke="var(--hex-line)" stroke-width="2" opacity="0.5"/>
    </svg>

    <h1>
      <span class="title-script">Youth</span>
      <span class="title-main">GROUP</span>
    </h1>

    <p class="schedule">SUNDAYS : 6-8PM</p>
    <p class="start-date">(Beginning April 14)</p>

    <div class="location-bar">
      <svg viewBox="0 0 24 32" aria-hidden="true">
        <path d="M12 0C5.4 0 0 5.3 0 11.9 0 20.8 12 32 12 32s12-11.2 12-20.1C24 5.3 18.6 0 12 0zm0 17a5 5 0 1 1 0-10 5 5 0 0 1 0 10z" fill="#d62d20"/>
      </svg>
      <span>Wexlander's - 4182 Quillon Ridge Ave N, Keizer, 97158</span>
    </div>

    <p class="offer-label">THERE WILL BE</p>
    <ul class="offer-tags" style="list-style:none">
      <li class="offer-tag"><span>DINNER</span></li>
      <li class="offer-tag"><span>GAMES</span></li>
      <li class="offer-tag"><span>FRIENDS</span></li>
      <li class="offer-tag"><span>A MESSAGE</span></li>
    </ul>
  </main>
</body>
</html>
```